Real estate broker business card

Want a modern celan but effective business card for my residential and commercial real estate business. I want the back of the card to advertise my services and to capture business. I have attached the back of my current business card fore ideas
Updates

Target Market(s)

home buyers and seller. commercial buyers and sellers

Industry/Entity Type

Real Estate

Contact Information for Business Card

must have my contact information and my photo

Requirements
Must have
• Lorna Vettridge
• Owner & Qualifying Broker
• Brockhill Real Estate Services
• 555.218.7094
• lorna@brockhillhomes.example
• www.brockhillhomes.example
Nice to have
• metallic
• Business capture text: " Don't buy or lease property without someone looking out for your best interests. I will represent you on your home or investment purchase for FREE!"
• "Home owners, call today to receive a FREE market analysis for your homes value!

```html
<!DOCTYPE html>
<html lang="en">
<head>
<meta charset="utf-8">
<title>Brockhill Real Estate Services – Business Card</title>
<link rel="stylesheet" href="https://fonts.googleapis.com/css2?family=Open+Sans:wght@400;600;700&display=swap">
<style>
  :root {
    --teal: #1f7f8c;
    --teal-dark: #136572;
    --teal-light: #2a9aa8;
    --ink: #454545;
    --paper: #ffffff;
    --night: #050505;
    --silver-1: #f4f4f4;
    --silver-2: #b9b9b9;
    --silver-3: #8c8c8c;
    --backdrop: #e7e4e0;
  }
  * { box-sizing: border-box; margin: 0; padding: 0; }
  html, body { width: 1200px; height: 1000px; overflow: hidden; }
  body {
    position: relative;
    background: var(--backdrop);
    font-family: "Open Sans", Arial, sans-serif;
  }
  .card {
    position: absolute;
    left: 265px;
    width: 666px;
    height: 397px;
    overflow: hidden;
    box-shadow: 0 4px 14px rgba(0,0,0,0.25);
  }
  .card--front { top: 73px; background: var(--paper); }
  .card--back { top: 532px; background: var(--night); }

  /* Front */
  .brand { position: absolute; display: flex; align-items: center; gap: 12px; }
  .brand__mark {
    width: 16px; height: 16px; border-radius: 50%;
    background: var(--teal); flex: none;
  }
  .brand__name { color: var(--teal); font-weight: 600; line-height: 1; }
  .brand__name .word { display: block; letter-spacing: 1px; }
  .brand__name .sub { display: block; letter-spacing: 3.2px; margin-top: 6px; }
  .card--front .brand { left: 33px; top: 80px; }
  .card--front .brand__name .word { font-size: 40px; }
  .card--front .brand__name .sub { font-size: 11px; }

  .pitch {
    position: absolute; left: 33px; top: 170px; width: 300px;
    font-size: 15px; line-height: 19px; color: var(--ink);
  }
  .contacts { position: absolute; left: 33px; top: 272px; list-style: none; }
  .contacts li {
    display: flex; align-items: center; gap: 9px;
    font-size: 16px; line-height: 24px; color: var(--ink);
  }
  .contacts svg { width: 14px; height: 14px; fill: var(--teal); flex: none; }

  .divider {
    position: absolute; left: 367px; top: 80px; width: 2px; height: 228px;
    background: linear-gradient(to bottom, rgba(31,127,140,0), var(--teal) 25%, var(--teal) 75%, rgba(31,127,140,0));
  }

  .portrait { position: absolute; left: 426px; top: 112px; width: 176px; height: 158px; }
  .person { position: absolute; left: 380px; top: 284px; width: 266px; text-align: center; }
  .person__name { font-size: 19px; font-weight: 700; color: var(--teal); letter-spacing: 0.5px; }
  .person__title { font-size: 16px; color: var(--ink); margin-top: 2px; }

  .band { position: absolute; left: 0; bottom: 0; width: 666px; height: 24px; }

  /* Back */
  .card--back .brand { left: 128px; top: 148px; gap: 18px; }
  .card--back .brand__mark { width: 22px; height: 22px; }
  .card--back .brand__name .word { font-size: 56px; }
  .card--back .brand__name .sub { font-size: 15px; letter-spacing: 4.4px; margin-top: 8px; }
  .offer {
    position: absolute; left: 0; top: 328px; width: 666px; text-align: center;
    font-size: 15px; line-height: 20px; color: var(--teal-light);
  }
</style>
</head>
<body>
  <section class="card card--front" aria-label="Business card front">
    <div class="brand">
      <span class="brand__mark"></span>
      <span class="brand__name"><span class="word">BROCKHILL</span><span class="sub">REAL ESTATE SERVICES</span></span>
    </div>

    <p class="pitch">Don't buy or lease property without someone looking out for your best interests. I will represent you on your home or investment purchase for FREE!</p>

    <ul class="contacts">
      <li><svg viewBox="0 0 16 16"><path d="M2 6c0-2 2-3 6-3s6 1 6 3v1h-3V5.5C10 5 6 5 5 5.5V7H2zM4 8h8l2 5H2z"/></svg>555.218.7094</li>
      <li><svg viewBox="0 0 16 16"><path d="M1 3h14v10H1zM2 4v1l6 4 6-4V4z" fill-rule="evenodd"/></svg>lorna@brockhillhomes.example</li>
      <li><svg viewBox="0 0 16 16"><path d="M8 1a7 7 0 1 0 0 14A7 7 0 0 0 8 1zm0 2a5 5 0 0 1 4.6 3H10L8 4 6 6H3.4A5 5 0 0 1 8 3zm-4.8 5h3.3l1.5 2-1 3a5 5 0 0 1-3.8-5zm6.3 4.8L10 10l2.8-2A5 5 0 0 1 9.5 12.8z"/></svg>www.brockhillhomes.example</li>
    </ul>

    <div class="divider"></div>

    <svg class="portrait" viewBox="0 0 176 158" role="img" aria-label="Portrait photo of Lorna Vettridge">
      <defs>
        <linearGradient id="portraitTone" x1="0" y1="0" x2="0" y2="1">
          <stop offset="0" stop-color="#2f3d25"/>
          <stop offset="0.55" stop-color="#5a4236"/>
          <stop offset="1" stop-color="#d9d6d2"/>
        </linearGradient>
      </defs>
      <path d="M0 0H176V70C176 118 140 146 88 158C36 146 0 118 0 70Z" fill="url(#portraitTone)"/>
    </svg>

    <div class="person">
      <p class="person__name">LORNA VETTRIDGE</p>
      <p class="person__title">Owner &amp; Qualifying Broker</p>
    </div>

    <svg class="band" viewBox="0 0 666 24" preserveAspectRatio="none" aria-hidden="true">
      <defs>
        <linearGradient id="silverBand" x1="0" y1="0" x2="1" y2="0">
          <stop offset="0" stop-color="#9a9a9a"/>
          <stop offset="0.3" stop-color="#f2f2f2"/>
          <stop offset="0.6" stop-color="#a8a8a8"/>
          <stop offset="1" stop-color="#e6e6e6"/>
        </linearGradient>
      </defs>
      <path d="M0 0H336L360 24H0Z" fill="var(--teal)"/>
      <path d="M350 0H360L384 24H374Z" fill="var(--teal)"/>
      <path d="M344 0H666V24H368Z" fill="url(#silverBand)"/>
    </svg>
  </section>

  <section class="card card--back" aria-label="Business card back">
    <div class="brand">
      <span class="brand__mark"></span>
      <span class="brand__name"><span class="word">BROCKHILL</span><span class="sub">REAL ESTATE SERVICES</span></span>
    </div>
    <p class="offer">Home owners, call today to receive a FREE market analysis<br>for your homes value!</p>
  </section>
</body>
</html>
```